Attorney business card for two offices

Looking for a new business card design that can list both of my offices, one in Houston and one in West Texas. Want something masculine, easy to read, and conservative yet somewhat modern. Our current card has used a nautical star on it for years, but I am not necessarily attached to that. Also, a lot of our forms use dark green and orange. Second office address is P.O. Box 518, Marathon, Texas 79617

```html
<!DOCTYPE html>
<html lang="en">
<head>
<meta charset="utf-8">
<title>The Mercer Law Firm, P.C. — Business Card</title>
<link rel="stylesheet" href="https://fonts.googleapis.com/css2?family=Roboto:wght@400;500;700&display=swap">
<style>
  :root {
    --backdrop: #dcdcdc;
    --card: #ffffff;
    --green-firm: #0d5a0d;
    --green-name: #0b3d0b;
    --green-band-dark: #0a340a;
    --green-band-light: #0c5c0c;
    --brown-title: #6b3a00;
    --ink: #444444;
    --ink-soft: #666666;
    --rule: #333333;
  }
  * { margin: 0; padding: 0; box-sizing: border-box; }
  html, body {
    width: 1200px;
    height: 999px;
    overflow: hidden;
    background: var(--backdrop);
    font-family: "Roboto", Arial, sans-serif;
  }
  .card {
    position: absolute;
    left: 100px;
    top: 214px;
    width: 1000px;
    height: 571px;
    background: var(--card);
  }
  .firm-name {
    position: absolute;
    right: 62px;
    top: 90px;
    font-size: 35px;
    font-weight: 700;
    color: var(--green-firm);
    letter-spacing: 0.2px;
  }
  .attorney {
    position: absolute;
    left: 61px;
    top: 276px;
  }
  .attorney-name {
    font-size: 32px;
    font-weight: 700;
    color: var(--green-name);
    line-height: 1.1;
  }
  .attorney-title {
    font-size: 22px;
    font-weight: 400;
    color: var(--brown-title);
    line-height: 1.2;
    margin-left: 1px;
  }
  .divider {
    position: absolute;
    left: 62px;
    right: 62px;
    top: 366px;
    height: 1px;
    background: var(--rule);
  }
  .office {
    position: absolute;
    font-size: 22px;
    line-height: 25px;
  }
  .office-main {
    left: 61px;
    top: 390px;
    color: var(--ink);
  }
  .contact {
    margin-top: 10px;
    line-height: 30px;
  }
  .office-west {
    right: 62px;
    top: 395px;
    text-align: right;
    color: var(--ink-soft);
  }
  .band {
    position: absolute;
    left: 0;
    right: 0;
    bottom: 0;
    height: 16px;
    background: linear-gradient(90deg, var(--green-band-dark), var(--green-band-light));
  }
</style>
</head>
<body>
  <div class="card">
    <div class="firm-name">The Mercer Law Firm, P.C.</div>

    <div class="attorney">
      <div class="attorney-name">Daniel T. Mercer, Sr.</div>
      <div class="attorney-title">Attorney At Law</div>
    </div>

    <div class="divider"></div>

    <div class="office office-main">
      <div>4410 Westway Park Blvd, Suite 220</div>
      <div>Houston, Texas 77024</div>
      <div class="contact">
        <div>P: (713) 555-0142 F: (832) 555-0187</div>
        <div>E: Daniel@Mercertxlaw.com W: Mercertxlaw.com</div>
      </div>
    </div>

    <div class="office office-west">
      <div>P.O. Box 518</div>
      <div>Marathon, Texas 79617</div>
    </div>

    <div class="band"></div>
  </div>
</body>
</html>
```